Website for AV installation with booking system and e-commerce

Company: Corvexa
Tag Line: Audio Visual and Security System Installations
We need a website for an AV company based in Sydney Australia. We specialise in Audio Visual, CCTV (security cameras), and Data Cabling.
The purpose of the website is that customers book their installation online with a live booking system.
We are looking for the following:
- Creative and modern design
- easy to use - keep in mind that the user who will book will have little knowledge in technology.
- clean and organised
- colours to work in well with our logo we also like royal to navy blue, but we are open to other suggested what works well with our logo.
We want customers to be able to add products needed for their installation ie when booking to wall mount their TV they can choose to add a TV bracket and cables to the cart and vise-versa buy a bracket or cables and add to cart the installation.
Tabs to be included:
About us
Gallery
Contact Us
Home
Services (there are three services that we offer - Residential, Corporate and Retail)
Products
Book Online/Cart (checkout)
Temporary website checkout: www.corvexa.com.au, please note this is very basic and we do not want a copy of this. This is purely to give you an idea of our company.
Good Luck!
Target Market(s)
home owners/renters, business owners, archiects/designers, builders
Industry/Entity Type
E-Commerce
Look and feel

```html
<!DOCTYPE html>
<html lang="en">
<head>
<meta charset="utf-8">
<title>Corvexa – Audio Visual and Security System Installations</title>
<link href="https://fonts.googleapis.com/css2?family=Open+Sans:wght@300;400;600;700;800&family=Ubuntu:wght@400;500;700&display=swap" rel="stylesheet">
<style>
:root{
  --red:#d3141b;
  --red-dark:#a80e14;
  --navy:#2f3373;
  --navy-light:#464b93;
  --navy-dark:#23265a;
  --ink:#333;
  --muted:#8a8a8a;
  --page-bg:#efefef;
  --card:#fff;
  --side:#3b3b3b;
  --side-line:#4a4a4a;
  --foot:#333333;
  --foot-link:#bdbdbd;
  --field:#1f1f1f;
}
*{box-sizing:border-box;margin:0;padding:0}
html,body{width:870px;height:1200px;overflow:hidden}
body{background:var(--page-bg);font-family:"Open Sans",sans-serif;color:var(--ink);position:relative}
a{color:inherit;text-decoration:none}

.page{position:absolute;left:81px;top:16px;width:709px;height:932px;background:var(--card);box-shadow:0 0 4px rgba(0,0,0,.08)}
.abs{position:absolute}

/* header */
.brand{left:13px;top:36px;display:flex;align-items:center;gap:8px;font-family:"Open Sans",sans-serif;font-weight:800;font-size:34px;color:var(--red);letter-spacing:-1px}
.brand-dot{width:14px;height:14px;border-radius:50%;background:var(--red)}
.cart-btn{left:571px;top:26px;width:123px;height:22px;background:var(--red);border:1px solid var(--red-dark);color:#fff;font-size:9.5px;display:flex;align-items:center;justify-content:center;gap:6px}
.contacts{right:15px;top:62px;display:flex;gap:16px;font-size:15px;color:var(--navy);font-weight:400}
.contacts span{display:flex;align-items:center;gap:4px}

/* nav */
.nav{left:13px;top:100px;width:682px;height:30px;background:linear-gradient(#4a4f95,#2f3373);border:1px solid var(--navy-dark);display:flex}
.nav a{display:flex;align-items:center;justify-content:center;color:#fff;font-size:12.5px;font-weight:300;border-right:1px solid rgba(255,255,255,.12);height:100%}
.nav a.active{background:#fff;color:var(--ink);font-weight:400;margin:2px 0 2px 2px;height:auto}

/* hero */
.hero{left:13px;top:138px;width:682px;height:289px;border-radius:3px;background:linear-gradient(120deg,#7d92a4 0%,#b9c8d4 40%,#dde4ea 62%,#8fa2b1 100%);overflow:hidden}
.hero h1{position:absolute;left:14px;top:96px;font-weight:800;font-size:26px;line-height:36px;color:#fff;letter-spacing:-1.2px;text-transform:uppercase;text-shadow:0 1px 3px rgba(0,0,0,.35)}
.hero .learn{position:absolute;left:14px;top:168px;width:134px;height:33px;background:var(--red);color:#fff;font-size:19px;display:flex;align-items:center;justify-content:center;border-radius:2px}

/* services strip */
.services{left:13px;top:434px;width:682px;height:58px;background:linear-gradient(#f4f4f4,#dcdcdc);border:1px solid #d0d0d0}
.svc{position:absolute;top:0;height:56px}
.svc h2{position:absolute;left:50px;top:6px;font-weight:700;font-size:19px;color:var(--navy);letter-spacing:-.3px}
.svc p{position:absolute;left:50px;top:30px;font-size:7.6px;line-height:10px;color:#222;width:170px}
.svc svg{position:absolute;left:16px;top:7px}
.chev{position:absolute;top:0}

/* welcome */
.welcome{left:13px;top:516px;width:682px}
.welcome h2{font-weight:400;font-size:20px;color:var(--red)}
.welcome p{margin-top:6px;font-size:10px;line-height:14px;color:var(--muted);height:42px;overflow:hidden}

/* categories */
.cats{left:13px;top:612px;width:160px;height:294px;background:var(--side)}
.cats h3{height:29px;background:linear-gradient(#fafafa,#e6e6e6);font-family:"Ubuntu",sans-serif;font-weight:700;font-size:17px;color:var(--red);padding:5px 7px;border:1px solid #ddd}
.cats li{list-style:none;height:29.4px;border-bottom:1px solid var(--side-line);display:flex;align-items:center;gap:7px;padding-left:6px;color:#fff;font-family:"Ubuntu",sans-serif;font-size:10.5px}
.cats li.open{background:#fff;color:var(--navy);border:1px solid #ddd;position:relative}
.cats li.open::after{content:"";position:absolute;right:5px;top:13px;border:3px solid transparent;border-top-color:var(--navy)}
.bullet{width:9px;height:9px;flex:none}

/* products */
.prod-title{left:185px;top:617px;font-family:"Ubuntu",sans-serif;font-weight:700;font-size:17px;color:var(--red)}
.prod-rule{left:291px;top:622px;width:404px;height:10px;background:repeating-linear-gradient(135deg,#e4e4e4 0 1px,#fff 1px 3px)}
.grid{left:185px;top:646px;width:510px;display:grid;grid-template-columns:repeat(4,122px);column-gap:7px;row-gap:9px}
.item{height:126px;border:1px solid #e6e6e6;background:#f8f8f8;padding:5px}
.item .photo{height:67px;border:1px solid #eee;border-radius:2px}
.item h4{font-weight:400;font-size:10px;margin-top:7px;color:#222}
.item .btns{display:flex;gap:5px;margin-top:7px}
.btn{height:17px;font-size:7px;color:#fff;display:flex;align-items:center;justify-content:center}
.btn.add{width:46px;background:var(--red)}
.btn.det{width:38px;background:var(--navy)}

/* footer */
.footer{position:absolute;left:81px;top:958px;width:709px;height:224px;background:var(--foot);border:1px solid #222;color:#fff}
.fcol{position:absolute;top:22px}
.fcol h5{font-family:"Ubuntu",sans-serif;font-weight:400;font-size:13.5px;margin-bottom:14px}
.fcol a{display:block;font-size:8.3px;color:var(--foot-link);text-decoration:underline;line-height:15.2px}
.field{width:132px;height:19px;background:var(--field);border:1px solid #111;border-radius:2px;font-size:8px;color:#888;padding:4px 7px;margin-bottom:8px}
.field.msg{height:47px}
.subscribe{width:53px;height:20px;background:#f2f2f2;color:#111;font-size:7.8px;font-weight:600;display:flex;align-items:center;justify-content:center;border-radius:2px;margin-top:-2px;margin-left:1px}
.fbottom{position:absolute;left:12px;right:15px;top:186px;border-top:1px solid #3f3f3f;padding-top:10px;display:flex;justify-content:space-between;font-size:9.3px;color:#ccc}
.fbottom nav{display:flex;gap:10px}
</style>
</head>
<body>
<div class="page">
  <div class="abs brand"><span>Corvexa</span><span class="brand-dot"></span></div>

  <a class="abs cart-btn" href="#">
    <svg width="16" height="12" viewBox="0 0 16 12" aria-hidden="true"><path d="M0 1h3l2 7h8l2-5H4" fill="none" stroke="#fff" stroke-width="1.3"/><circle cx="6" cy="10.5" r="1.2" fill="#fff"/><circle cx="12" cy="10.5" r="1.2" fill="#fff"/></svg>
    Shopping Cart - $0.00
  </a>

  <div class="abs contacts">
    <span><svg width="12" height="13" viewBox="0 0 12 13" aria-hidden="true"><path d="M2 1l2.5 0 1 3-1.5 1.2c.8 1.8 2 3 3.6 3.7L9 7.4l3 1v2.5c0 .8-1 1.3-2 1C5 10.8 1.5 7 1 3 .9 2 1.2 1 2 1z" fill="#2f3373"/></svg>(02) 5550 1234</span>
    <span><svg width="9" height="13" viewBox="0 0 9 13" aria-hidden="true"><rect x=".5" y=".5" width="8" height="12" rx="1" fill="none" stroke="#2f3373"/><rect x="2" y="2" width="5" height="4" fill="#2f3373"/><path d="M2 8h1M4 8h1M6 8h1M2 10h1M4 10h1M6 10h1" stroke="#2f3373"/></svg>0400 555 019</span>
  </div>

  <nav class="abs nav">
    <a class="active" href="#" style="width:65px">Home</a>
    <a href="#" style="width:105px">About us</a>
    <a href="#" style="width:92px">Services</a>
    <a href="#" style="width:108px">Gallery</a>
    <a href="#" style="width:116px">Book Online</a>
    <a href="#" style="width:111px">Products</a>
    <a href="#" style="width:83px;border-right:0">Contact Us</a>
  </nav>

  <section class="abs hero">
    <div role="img" aria-label="Photo of a white security camera mounted on a pole in front of a glass building with scaffolding" style="position:absolute;inset:0"></div>
    <h1>Audio Visual and Security<br>System Installations</h1>
    <a class="learn" href="#">Learn More</a>
  </section>

  <section class="abs services">
    <div class="svc" style="left:0;width:320px">
      <svg width="26" height="22" viewBox="0 0 26 22" aria-hidden="true"><path d="M13 1L1 11h3v10h7v-6h4v6h7V11h3z" fill="#d3141b"/></svg>
      <h2>RESIDENTIAL</h2>
      <p>Le Lorem Ipsum est simplement du faux texte employé dans la composition.</p>
    </div>
    <svg class="chev" style="left:224px" width="16" height="56" viewBox="0 0 16 56" aria-hidden="true"><path d="M2 0l12 28L2 56" fill="none" stroke="#c4c4c4" stroke-width="2"/></svg>
    <div class="svc" style="left:234px;width:220px">
      <svg width="26" height="22" viewBox="0 0 26 22" aria-hidden="true"><g fill="#d3141b"><circle cx="6" cy="4" r="3"/><circle cx="13" cy="4" r="3"/><circle cx="20" cy="4" r="3"/><rect x="3" y="8" width="6" height="13" rx="1"/><rect x="10" y="8" width="6" height="13" rx="1"/><rect x="17" y="8" width="6" height="13" rx="1"/></g></svg>
      <h2>CORPORATE</h2>
      <p>Le Lorem Ipsum est simplement du faux texte employé dans la composition.</p>
    </div>
    <svg class="chev" style="left:446px" width="16" height="56" viewBox="0 0 16 56" aria-hidden="true"><path d="M2 0l12 28L2 56" fill="none" stroke="#c4c4c4" stroke-width="2"/></svg>
    <div class="svc" style="left:458px;width:224px">
      <svg width="26" height="22" viewBox="0 0 26 22" aria-hidden="true"><path d="M1 2h4l3 11h13l3-8H7" fill="none" stroke="#d3141b" stroke-width="2.4"/><circle cx="10" cy="18" r="2" fill="#d3141b"/><circle cx="19" cy="18" r="2" fill="#d3141b"/></svg>
      <h2>RETAIL</h2>
      <p>Le Lorem Ipsum est simplement du faux texte employé dans la composition.</p>
    </div>
  </section>

  <section class="abs welcome">
    <h2>Welcome to Corvexa</h2>
    <p>Le Lorem Ipsum est simplement du faux texte employé dans la composition et la mise en page avant impression. Le Lorem Ipsum est le faux texte standard de l'imprimerie depuis les années 1500, quand un peintre anonyme assembla ensemble des morceaux de texte pour réaliser un livre spécimen de polices de texte. Il n'a pas fait que survivre cinq siècles, mais s'est aussi adapté à la bureautique informatique, sans que son contenu n'en soit modifié.</p>
  </section>

  <aside class="abs cats">
    <h3>CATEGORIES</h3>
    <ul>
      <li><svg class="bullet" viewBox="0 0 10 10" aria-hidden="true"><circle cx="5" cy="5" r="5" fill="#fff"/><path d="M4 3l3 2-3 2z" fill="#3b3b3b"/></svg>Corporate Gifts</li>
      <li class="open"><svg class="bullet" viewBox="0 0 10 10" aria-hidden="true"><circle cx="5" cy="5" r="5" fill="#2f3373"/><path d="M4 3l3 2-3 2z" fill="#fff"/></svg>apparues avec</li>
      <li><svg class="bullet" viewBox="0 0 10 10" aria-hidden="true"><circle cx="5" cy="5" r="5" fill="#fff"/><path d="M4 3l3 2-3 2z" fill="#3b3b3b"/></svg>trouvées ici</li>
      <li><svg class="bullet" viewBox="0 0 10 10" aria-hidden="true"><circle cx="5" cy="5" r="5" fill="#fff"/><path d="M4 3l3 2-3 2z" fill="#3b3b3b"/></svg>Contrairement à une</li>
      <li><svg class="bullet" viewBox="0 0 10 10" aria-hidden="true"><circle cx="5" cy="5" r="5" fill="#fff"/><path d="M4 3l3 2-3 2z" fill="#3b3b3b"/></svg>du Lorem Ipsum</li>
      <li><svg class="bullet" viewBox="0 0 10 10" aria-hidden="true"><circle cx="5" cy="5" r="5" fill="#fff"/><path d="M4 3l3 2-3 2z" fill="#3b3b3b"/></svg>proviennent de la</li>
      <li><svg class="bullet" viewBox="0 0 10 10" aria-hidden="true"><circle cx="5" cy="5" r="5" fill="#fff"/><path d="M4 3l3 2-3 2z" fill="#3b3b3b"/></svg>dictionnaire de</li>
      <li><svg class="bullet" viewBox="0 0 10 10" aria-hidden="true"><circle cx="5" cy="5" r="5" fill="#fff"/><path d="M4 3l3 2-3 2z" fill="#3b3b3b"/></svg>découvrit la source</li>
      <li style="border-bottom:0"><svg class="bullet" viewBox="0 0 10 10" aria-hidden="true"><circle cx="5" cy="5" r="5" fill="#fff"/><path d="M4 3l3 2-3 2z" fill="#3b3b3b"/></svg>utilisé depuis le</li>
    </ul>
  </aside>

  <h3 class="abs prod-title">PRODUCTS</h3>
  <div class="abs prod-rule"></div>

  <div class="abs grid">
    <div class="item"><div class="photo" role="img" aria-label="Product photo: cheese board with knives" style="background:radial-gradient(#e6c98e,#f7f2e8)"></div><h4>Cheese Sets</h4><div class="btns"><span class="btn add">Add to Cart</span><span class="btn det">Details</span></div></div>
    <div class="item"><div class="photo" role="img" aria-label="Product photo: outdoor picnic set in a black case" style="background:radial-gradient(#3a3a3a,#f2f2f2 80%)"></div><h4>Picnic, Outdoor</h4><div class="btns"><span class="btn add">Add to Cart</span><span class="btn det">Details</span></div></div>
    <div class="item"><div class="photo" role="img" aria-label="Product photo: navy polka-dot umbrella" style="background:radial-gradient(#1e2f52,#f4f4f4 75%)"></div><h4>Umbrellas</h4><div class="btns"><span class="btn add">Add to Cart</span><span class="btn det">Details</span></div></div>
    <div class="item"><div class="photo" role="img" aria-label="Product photo: pedometer with earphones" style="background:radial-gradient(#c33,#ddd 45%,#fff 80%)"></div><h4>Sports Products</h4><div class="btns"><span class="btn add">Add to Cart</span><span class="btn det">Details</span></div></div>
    <div class="item"><div class="photo" role="img" aria-label="Product photo: green gardening tool set" style="background:radial-gradient(#3d8a4e,#f4f4f4 80%)"></div><h4>Gardening Set</h4><div class="btns"><span class="btn add">Add to Cart</span><span class="btn det">Details</span></div></div>
    <div class="item"><div class="photo" role="img" aria-label="Product photo: black and blue promotional cap" style="background:radial-gradient(#1c1c1c,#f4f4f4 78%)"></div><h4>Promotional Cap</h4><div class="btns"><span class="btn add">Add to Cart</span><span class="btn det">Details</span></div></div>
    <div class="item"><div class="photo" role="img" aria-label="Product photo: blue tote bag" style="background:radial-gradient(#2a6fd0,#f4f4f4 75%)"></div><h4>Bags</h4><div class="btns"><span class="btn add">Add to Cart</span><span class="btn det">Details</span></div></div>
    <div class="item"><div class="photo" role="img" aria-label="Product photo: row of coloured drink bottles" style="background:linear-gradient(90deg,#f3c21a,#d3141b 35%,#e8e8e8 60%,#2d4fa8 85%)"></div><h4>Bottles</h4><div class="btns"><span class="btn add">Add to Cart</span><span class="btn det">Details</span></div></div>
  </div>
</div>

<footer class="footer">
  <div class="fcol" style="left:12px"><h5>Home</h5><a href="#">Contrairement</a><a href="#">Opinion répandue</a><a href="#">Pas simplement du</a><a href="#">Texte aléatoire</a></div>
  <div class="fcol" style="left:145px"><h5>Residential</h5><a href="#">Vous voulez utiliser</a><a href="#">Passage du Lorem</a><a href="#">Vous devez être sûr</a><a href="#">Qu'il n'y a rien</a><a href="#">Embarrassant caché</a><a href="#">Dans le texte.</a><a href="#">Générateurs de Lorem</a></div>
  <div class="fcol" style="left:290px"><h5>Corporate</h5><a href="#">Plusieurs variations</a><a href="#">De Lorem Ipsum</a><a href="#">Vent être</a></div>
  <div class="fcol" style="left:429px"><h5>Retail</h5><a href="#">L'extrait standard</a><a href="#">Utilisé depuis</a><a href="#">Siècle est reproduit</a><a href="#">Dessous pour les</a><a href="#">Curieux</a><a href="#">Vous voulez utiliser</a><a href="#">Passage du Lorem</a></div>
  <div class="fcol" style="left:557px"><h5>Customer Feedback</h5>
    <div class="field">Name</div>
    <div class="field">Email</div>
    <div class="field msg">Message</div>
    <div class="subscribe">Subscribe</div>
  </div>
  <div class="fbottom">
    <nav><a href="#">About us</a><a href="#">Gallery</a><a href="#">Contact Us</a><a href="#">Home</a><a href="#">Services</a><a href="#">Products</a><a href="#">Book Online</a></nav>
    <span>© Copyrights 2013 All rights Reserved</span>
  </div>
</footer>
</body>
</html>
```